Disease outbreak warning

I need a flyer that explains to hunters how to act as frontline responders to potential disease outbreaks in wildlife populations. In this case the disease is African Swine Fever. We need an at a glance style with plenty of colour and that’s very easy to read.

I HAVE ATTACHED SOME EXISTING FLYERS FROM OVERSEAS ETC THAT CONTAIN SOME OF THE RELEVANT INFO. THEY ARE TO BE USED AS A GUIDE ONLY.
Updates

Need to see some more options. We have some that can be developed successfully but we’d like to see some more options that will suit a national campaign.

Target Market(s)

Australian hunters encountering wild pigs. Typical age is from 18 to 32 but can be older. Male or female.

Colors

Designer to choose colors to be used in the design.

Requirements
Must have
• The KVRTE logo (supplied). It should be relatively small at the bottom of the page. Plus we need room for two or three other logos that can be overprinted on the project if required.
• Must have information for hunters as the main focus.
Nice to have
• A double sided flyer.
Should not have
• US spelling.

```html
<!DOCTYPE html>
<html lang="en-AU">
<head>
<meta charset="utf-8">
<title>African Swine Fever – Hunter Flyer</title>
<link rel="stylesheet" href="https://fonts.googleapis.com/css2?family=Open+Sans:wght@700;800&family=PT+Sans+Narrow:wght@400;700&display=swap">
<style>
  :root {
    --ink: #0b0b0b;
    --forest: #10614f;
    --forest-dark: #0c4a3c;
    --cream: #fdf8ea;
    --cream-edge: #eadcbf;
    --white: #ffffff;
    --stage: #3d5a5d;
    --autumn-light: #d9a070;
    --autumn-mid: #a8683a;
    --autumn-dark: #5a3820;
  }
  * { margin: 0; padding: 0; box-sizing: border-box; }
  html, body { width: 1200px; height: 776px; overflow: hidden; }
  body { background: var(--stage); position: relative; font-family: "PT Sans Narrow", "Arial Narrow", sans-serif; }

  .flyer { position: absolute; top: 28px; width: 520px; height: 720px; overflow: hidden; box-shadow: 0 6px 18px rgba(0,0,0,.35); }
  .flyer--front { left: 50px; }
  .flyer--back { left: 630px; background: radial-gradient(ellipse at 60% 45%, var(--cream) 55%, var(--cream-edge) 100%); }

  .photo-area { position: absolute; inset: 0;
    background: linear-gradient(175deg, var(--autumn-light) 0%, #c48a5a 35%, var(--autumn-mid) 65%, var(--autumn-dark) 100%); }

  .headline { position: absolute; text-align: right; font-family: "Open Sans", sans-serif; font-weight: 800; line-height: .95; white-space: nowrap; }
  .headline__main { display: block; font-size: 66px; letter-spacing: -1px; }
  .headline__sub { display: block; font-size: 40px; }
  .tagline { display: block; font-family: "PT Sans Narrow", sans-serif; font-weight: 700; font-size: 24px; margin-top: 6px; }

  .flyer--front .headline { top: 30px; right: 24px; color: var(--ink); }
  .intro { position: absolute; top: 180px; right: 24px; width: 330px; text-align: right; color: var(--white); font-size: 17px; line-height: 1.15; }

  .frame-shapes { position: absolute; inset: 0; }

  .member-seal { position: absolute; display: flex; align-items: center; justify-content: center;
    border-radius: 50%; background: var(--white); font-family: "Open Sans", sans-serif; font-weight: 800; color: var(--forest-dark); }
  .flyer--front .member-seal { left: 50px; top: 470px; width: 180px; height: 180px; border: 12px solid var(--forest); font-size: 34px; }
  .flyer--back .member-seal { right: 18px; top: 14px; width: 112px; height: 112px; font-size: 22px; }

  .steps { position: absolute; left: 26px; top: 36px; list-style: none; }
  .step { position: relative; height: 104px; display: flex; align-items: center; }
  .step__badge { width: 78px; height: 78px; flex: none; }
  .step__text { margin-left: 18px; font-size: 20px; font-weight: 700; line-height: 1.05; color: var(--ink); width: 150px; }
  .steps__spine { position: absolute; left: 60px; top: 0; width: 10px; height: 650px; background: var(--forest); }

  .flyer--back .headline { right: 24px; top: 500px; color: var(--forest); }
  .flyer--back .headline__main { font-size: 54px; }
  .flyer--back .headline__sub { font-size: 34px; }
  .flyer--back .tagline { color: var(--ink); font-size: 21px; }

  .contact-bar { position: absolute; left: 0; right: 0; bottom: 0; height: 74px; background: var(--ink); color: var(--white);
    display: flex; justify-content: space-between; align-items: center; padding: 0 22px; font-weight: 700; font-size: 25px; white-space: nowrap; }
  .contact-bar__web { font-size: 22px; }
</style>
</head>
<body>

<section class="flyer flyer--front">
  <div class="photo-area" role="img" aria-label="Photograph of a wild boar walking through autumn leaf litter in woodland"></div>
  <svg class="frame-shapes" width="520" height="720" viewBox="0 0 520 720">
    <polygon points="0,420 0,720 340,720" fill="#0b0b0b"/>
    <line x1="0" y1="385" x2="350" y2="720" stroke="#10614f" stroke-width="12"/>
  </svg>
  <h1 class="headline">
    <span class="headline__main">African</span>
    <span class="headline__sub">swine fever</span>
    <span class="tagline">Don’t spreade this deadly disease</span>
  </h1>
  <p class="intro">Lorem ipsum dolor sit amet, consectetur adipiscing elit, sed do eiusmod tempor incididunt ut labore et dolore magna aliqua.</p>
  <div class="member-seal">KVRTE</div>
</section>

<section class="flyer flyer--back">
  <svg class="frame-shapes" width="520" height="720" viewBox="0 0 520 720">
    <polygon points="220,0 520,0 520,190" fill="#0b0b0b"/>
    <line x1="190" y1="0" x2="520" y2="215" stroke="#10614f" stroke-width="10"/>
  </svg>
  <div class="member-seal">KVRTE</div>

  <div class="steps__spine"></div>
  <ol class="steps">
    <li class="step">
      <svg class="step__badge" viewBox="0 0 80 80" aria-hidden="true">
        <polygon points="40,2 73,21 73,59 40,78 7,59 7,21" fill="#10614f"/>
        <path d="M32 24h16v8l6 6v20H26V38l6-6z" fill="#fff"/>
        <rect x="36" y="18" width="8" height="6" fill="#fff"/>
      </svg>
      <span class="step__text">Clean &amp; disinfect your equipment on site</span>
    </li>
    <li class="step">
      <svg class="step__badge" viewBox="0 0 80 80" aria-hidden="true">
        <polygon points="40,2 73,21 73,59 40,78 7,59 7,21" fill="#10614f"/>
        <path d="M18 40L40 22l22 18v18H18z" fill="#fff"/>
        <rect x="33" y="44" width="14" height="14" fill="#10614f"/>
      </svg>
      <span class="step__text">Do not visit farms unless it is necessary</span>
    </li>
    <li class="step">
      <svg class="step__badge" viewBox="0 0 80 80" aria-hidden="true">
        <polygon points="40,2 73,21 73,59 40,78 7,59 7,21" fill="#10614f"/>
        <rect x="22" y="30" width="36" height="26" rx="3" fill="#fff"/>
        <rect x="33" y="23" width="14" height="8" rx="2" fill="none" stroke="#fff" stroke-width="3"/>
      </svg>
      <span class="step__text">Do not carry pigs or pork products</span>
    </li>
    <li class="step">
      <svg class="step__badge" viewBox="0 0 80 80" aria-hidden="true">
        <polygon points="40,2 73,21 73,59 40,78 7,59 7,21" fill="#10614f"/>
        <rect x="36" y="16" width="8" height="34" rx="4" fill="#fff"/>
        <circle cx="40" cy="54" r="9" fill="#fff"/>
        <rect x="38.5" y="30" width="3" height="22" fill="#c0282d"/>
        <circle cx="40" cy="54" r="5" fill="#c0282d"/>
      </svg>
      <span class="step__text">Report soon for sick pigs</span>
    </li>
    <li class="step">
      <svg class="step__badge" viewBox="0 0 80 80" aria-hidden="true">
        <polygon points="40,2 73,21 73,59 40,78 7,59 7,21" fill="#10614f"/>
        <path d="M40 18c8 12 14 20 14 28a14 14 0 0 1-28 0c0-8 6-16 14-28z" fill="#fff"/>
      </svg>
      <span class="step__text">Clean &amp; disinfect your hunting trophies before living the area</span>
    </li>
  </ol>

  <h2 class="headline">
    <span class="headline__main">African</span>
    <span class="headline__sub">swine fever</span>
    <span class="tagline">Don’t spreade this deadly disease</span>
  </h2>

  <footer class="contact-bar">
    <span class="contact-bar__phone">Call us : 123-456-7890</span>
    <span class="contact-bar__web">Website : swinewatch-au.org</span>
  </footer>
</section>

</body>
</html>
```